Quarrytide
Quarrytide - Financial Services
Financial Services
www.quarrytidepay.com
Our team has been providing solutions for workers compensation for business owners for over 22 years, our service is provoided at no charge (as it is paid for by the vendor). What makes us unique is our ability to write just about every size company (3 man to 1000) and industry in every state,. Our programs simlyfy the business owners way of doing business by eliminationg several annoying functions that business owners face. For example, with our program a business owner would write one check for payroll, that check would cover his payroll, workers compensation, payroll taxes, employee deductions and garnishments, direct deposit and benefit deductions, year end W-2's and the liabilities that come with year end W-2's. Our program we keeps business owners compliant by keeping them informed about new requirements, labor laws, we provide all employee applications, safety posters, they are able to call with any employee related questions about hiring and firing and so on. All usually for less that they can do it themselves.
Busy, wordy
Service Oriented
White/possible grey, logo colors
Blues and whites and greys, logo colors
left side
We have a content writer completing the text, our home page will contain very little text and focus more as a landing page. The site itself needs to be very clean, simple and easy to navigate but will also allow viewers to go deep into the site if they want to find information, yet at the same time it will not force people away because of too much content

```html
<!DOCTYPE html>
<html lang="en">
<head>
<meta charset="utf-8">
<title>Quarrytide - Financial Services</title>
<link href="https://fonts.googleapis.com/css2?family=Arimo:wght@400;700&display=swap" rel="stylesheet">
<style>
:root{
  --ink:#1b1f24;
  --topbar:#1c2024;
  --page-dark:#343c45;
  --header-light:#eceef1;
  --brand:#1d6fa5;
  --teal:#2a86ab;
  --teal-dark:#1f6c8c;
  --pill:#9ba5ae;
  --panel-grey:#6a7580;
  --panel-mid:#c9ced3;
  --white:#ffffff;
  --muted:#5a636c;
}
*{box-sizing:border-box;margin:0;padding:0}
html,body{width:1200px;height:838px;overflow:hidden}
body{font-family:"Arimo",Arial,sans-serif;color:var(--ink);
  background:linear-gradient(var(--topbar) 0 22px,var(--header-light) 22px 149px,var(--page-dark) 149px);position:relative}
.topbar{position:absolute;top:0;right:108px;height:22px;display:flex;align-items:center;gap:10px;font-size:11px;color:#dfe3e7}
.topbar .sep{color:#7d858d}
.site-header{position:absolute;left:108px;top:22px;width:984px;height:127px}
.brand{position:absolute;left:22px;top:18px;display:flex;align-items:center;gap:12px}
.brand-mark{width:48px;height:48px;border-radius:50%;background:var(--brand)}
.brand-name{font-size:38px;font-weight:700;color:var(--brand);letter-spacing:1px}
.brand-url{position:absolute;left:82px;top:70px;font-size:11px;color:var(--muted)}
.tagline{position:absolute;right:14px;top:6px;font-size:11px;color:var(--brand)}
.main-nav{position:absolute;right:16px;top:82px;display:flex;gap:6px}
.main-nav a{display:block;padding:5px 14px;border-radius:12px;background:var(--pill);color:var(--white);font-size:12px;text-decoration:none;border:1px solid #7e8992}
.main-nav a.active{background:var(--teal);border-color:var(--teal-dark)}
.hero{position:absolute;left:108px;top:149px;width:984px;height:223px;background:var(--white)}
.hero-photo{position:absolute;left:0;top:0;width:492px;height:223px;background:linear-gradient(120deg,#c9d2da,#8fa3b5 55%,#e8ecef)}
.hero-badge{position:absolute;left:352px;top:96px;width:136px;height:62px;border-radius:14px;background:var(--teal-dark);color:var(--white);padding:7px 10px;font-size:13px;line-height:1.15;white-space:nowrap}
.hero-badge b{font-size:22px;display:block;line-height:1.2}
.hero-title{position:absolute;left:505px;top:88px;font-size:29px;font-weight:700;letter-spacing:.3px;white-space:nowrap}
.hero-text{position:absolute;right:18px;top:132px;width:300px;font-size:9px;line-height:1.35;color:var(--muted);text-align:right}
.columns{position:absolute;left:108px;top:384px;width:984px;height:336px;display:flex;gap:8px}
.col{height:100%;position:relative}
.col-head{height:20px;background:var(--teal);color:var(--white);font-size:11px;font-weight:700;display:flex;align-items:center;justify-content:space-between;padding:0 8px}
.col-head small{font-size:8px;font-weight:400}
.news{width:392px;background:var(--panel-grey)}
.news-list{padding:6px 8px}
.news-item{color:var(--white);font-size:10px;margin-bottom:10px}
.news-item .date{color:#9fd3ea;font-weight:700;font-size:10px}
.news-item .headline{font-weight:700;margin-top:2px}
.news-featured{background:var(--white);color:var(--ink);padding:6px;display:flex;gap:8px;font-size:10px;line-height:1.35;margin:4px 0 12px}
.news-thumb{width:92px;height:70px;flex:none;background:linear-gradient(135deg,#dfe5ea,#9eafbd)}
.read-more{font-weight:700;color:var(--ink)}
.about{width:340px;background:var(--white)}
.about p{padding:10px 14px;font-size:10px;line-height:1.4;color:var(--muted)}
.team-photo{margin:4px 14px;height:150px;background:linear-gradient(#e4e8ec,#7e8c99 70%,#b9c2ca);position:relative}
.team-caption{position:absolute;left:50%;top:58px;transform:translateX(-50%);background:var(--teal-dark);color:var(--white);font-size:9px;font-weight:700;padding:3px 14px;text-align:center;white-space:nowrap}
.services{width:236px;background:var(--panel-mid)}
.services ul{list-style:none;padding:6px}
.svc{background:var(--white);color:var(--teal-dark);font-size:10px;font-weight:700;padding:4px 8px;margin-bottom:5px;border-left:4px solid var(--teal)}
.svc-sub{font-weight:400;color:var(--muted);padding:2px 0 2px 26px;font-size:9px}
.message-box{margin:8px 6px;height:44px;background:var(--white);display:flex;align-items:center;gap:12px;padding:0 10px;color:var(--teal-dark);font-weight:700;font-size:11px}
.message-thumb{width:52px;height:34px;background:linear-gradient(#c7d2dc,#7f93a4)}
.site-footer{position:absolute;left:108px;top:728px;width:984px;height:48px;background:var(--header-light);display:flex;align-items:center;justify-content:space-between;padding:0 20px 0 380px;font-size:10px;color:var(--muted)}
.social{display:flex;gap:4px}
.social span{width:14px;height:14px;background:var(--teal);border-radius:2px;display:block}
</style>
</head>
<body>
<nav class="topbar"><span>About us</span><span class="sep">|</span><span>Contact us</span><span class="sep">|</span><span>English</span><span class="sep">|</span><span>French</span></nav>

<header class="site-header">
  <div class="brand"><span class="brand-mark"></span><span class="brand-name">QUARRYTIDE</span></div>
  <div class="brand-url">www.quarrytidepay.com</div>
  <div class="tagline">We Think Financial support</div>
  <nav class="main-nav">
    <a href="#">ABOUT US</a><a href="#">NEWS</a><a class="active" href="#">SERVICES</a><a href="#">PROJECTS</a><a href="#">GALLERY</a><a href="#">CONTACT US</a>
  </nav>
</header>

<section class="hero">
  <div class="hero-photo" role="img" aria-label="Photo of a smiling businesswoman at a laptop with colleagues in an office"></div>
  <div class="hero-badge">What are you<b>looking for?</b></div>
  <h1 class="hero-title">WELCOME TO OUR'S SERVICE !</h1>
  <p class="hero-text">One check covers your payroll, workers compensation, payroll taxes and employee deductions, while our team keeps you compliant with new requirements and labor laws, so you can focus on growing your business.</p>
</section>

<main class="columns">
  <section class="col news">
    <div class="col-head">COMPANY NEWS / PROJECTS <small>HOME</small></div>
    <div class="news-list">
      <div class="news-item"><div class="date">22/08/2011</div><div class="headline">Understanding your business is a key part of our process.</div></div>
      <div class="news-featured">
        <div class="news-thumb" role="img" aria-label="Photo of hands working with papers and a pen"></div>
        <div>Understanding your business is a key part of our process, it lets us tailor our designs to meet your unique business needs. You'll love knowing you have full control of your project, without having to shoulder the burden of the strategy. Our s..... <span class="read-more">read more</span></div>
      </div>
      <div class="news-item"><div class="date">21/08/2011</div><div class="headline">Understanding your business is a key part of our process.</div></div>
      <div class="news-item"><div class="date">20/08/2011</div><div class="headline">Understanding your business is a key part of our process.</div></div>
      <div class="news-item"><div class="date">19/08/2011</div><div class="headline">Understanding your business is a key part of our process.</div></div>
    </div>
  </section>

  <section class="col about">
    <div class="col-head">ABOUT US <small>HOME</small></div>
    <p>After all, nothing is more important than the overall quality of your logo. Unlike many design firms, we employ a logo design process based on teams of designers. Because of the variety of designs you'll get, there is a better chance we'll find that perfect design you're hoping for. We put two to five logo designers on every custom logo design project. After you get your first concepts you'll know you made the right choice......</p>
    <div class="team-photo" role="img" aria-label="Photo of a business team standing together">
      <div class="team-caption">WELCOME<br>to the financial support</div>
    </div>
  </section>

  <section class="col services">
    <div class="col-head">OUR SERVICES <small>HOME</small></div>
    <ul>
      <li class="svc">BANK SERVICE
        <div class="svc-sub">Payroll Banking</div>
        <div class="svc-sub">Direct Deposit</div>
        <div class="svc-sub">Tax Filing</div>
        <div class="svc-sub">Benefit Deductions</div>
        <div class="svc-sub">Year End</div>
      </li>
      <li class="svc">TECHNICAL SUPPORT</li>
      <li class="svc">PERSONNEL TRAINING</li>
      <li class="svc">PROJECT MANAGEMENT</li>
    </ul>
    <div class="message-box"><span class="message-thumb" role="img" aria-label="Photo of a support agent"></span>MESSAGE</div>
  </section>
</main>

<footer class="site-footer">
  <span>© 2011 Quarrytide All Rights Reserved</span>
  <div class="social"><span></span><span></span><span></span><span></span><span></span><span></span><span></span><span></span><span></span><span></span><span></span><span></span></div>
</footer>
</body>
</html>
```